Project VELI

I am setting up a consultancy company in Istanbul, Turkey called VELI Partners. VELI partners will focus areas are highlighted in the attached presenatation. Expertise area as follows; Corporate Communications, Digitilization and Technology Integration, CSR & Sponsorships, Investor Relations and Fİnancial PR, Strategic Transactions, Corporate Governance... In related arease Project Management and Training support given.. For details see presenations. Our company collars are marun and blue.. In the attached presenations you can also see the business card colars and logo design. The design should reflect innovationi technology knowhow and power of communications skills. Enclosed you can find a presentations of scope of consultancy services and corporate logo from which logo and colars can be adapted..

Target Market(s)

Potential clients are any Holding or Company that would need services defined in the presantation attached.

Industry/Entity Type

It Company

Coding

Coded - Design and coding required

Number of Pages Required

5+ page

Font styles to use
Sans Serif

Requirements
Must have
• Main Expertize areas are defined in the presentation. The clients should be able to clearly see these and as they select the related area go to related page to see the content detail. I should be to also include vision statement in front page.. I should be able to present partners of the company in a related section. site should allow posting of pictures and an introductory video... Please use the logo and colars ı provided on attached file. Marun should be the dominating colar.
Nice to have
• www.morvanthrel.com I like.. Morvant provides somewhat similar services world wide. You can check out the site but don't need to necessarly do the same..

```html
<!DOCTYPE html>
<html lang="en">
<head>
<meta charset="utf-8">
<title>Contact – VELI Partners</title>
<link rel="stylesheet" href="https://fonts.googleapis.com/css2?family=Open+Sans:wght@400;600&family=Rajdhani:wght@400;500&display=swap">
<style>
:root{
  --maroon:#74004f;
  --plum:#a8288f;
  --plum-light:#b94ba1;
  --magenta:#b0106a;
  --navy:#1e2b8a;
  --ink:#333;
  --grey-panel:#ececec;
  --grey-field:#e6e4e5;
  --grey-band:#e8e8e8;
}
*{box-sizing:border-box;margin:0;padding:0}
html,body{width:1200px;height:1095px;overflow:hidden}
body{position:relative;background:#fff;font-family:Arial,"Open Sans",sans-serif;color:var(--ink)}
.abs{position:absolute}

/* header */
.brand{left:130px;top:14px;display:flex;align-items:center;gap:8px;font-family:"Open Sans",sans-serif;font-weight:600;font-size:26px;color:var(--navy);letter-spacing:1px}
.brand-dot{width:14px;height:14px;border-radius:50%;background:var(--navy)}
.top-nav{left:405px;top:0;width:795px;height:31px;background:var(--plum);border-bottom-left-radius:8px;box-shadow:0 2px 3px rgba(0,0,0,.2)}
.top-nav a{position:absolute;top:9px;font-size:11px;color:#fff;text-decoration:none;letter-spacing:.5px}
.dropdown{left:680px;top:31px;width:136px;height:57px;background:var(--plum-light);padding:5px 17px;font-size:11.5px;color:#fff;line-height:19px}
.search{left:870px;top:45px;width:201px;height:26px;border:1px solid #ddd;border-radius:3px;background:#fff;font-size:12px;color:#888;padding:5px 10px}
.search-btn{position:absolute;right:3px;top:2px;width:36px;height:20px;background:#c0278f;border-radius:2px}

/* service band */
.services{left:0;top:80px;width:1200px;height:72px;background:linear-gradient(#e4e4e6,#f8f8f8);border-bottom:4px solid #9b1a80}
.service{position:absolute;top:17px;line-height:17px}
.service b{display:block;font-family:"Open Sans",sans-serif;font-weight:600;font-size:14px;color:#a0006e}
.service span{font-size:12.5px;color:#555;letter-spacing:.5px}
.sep{position:absolute;top:16px;height:40px;border-left:1px dotted #bbb}

/* page title */
.title-band{left:0;top:156px;width:1200px;height:99px;background:var(--maroon)}
.title-decor{left:520px;top:0;width:620px;height:99px;background:radial-gradient(circle at 70% 40%,rgba(255,255,255,.16),rgba(255,255,255,0) 60%)}
.page-title{left:130px;top:24px;font-family:"Rajdhani",sans-serif;font-size:42px;color:#fff;letter-spacing:2px}

/* intro */
.intro{left:131px;top:313px;font-size:15px;line-height:29px;color:var(--ink)}
.intro a{color:var(--maroon);text-decoration:none}

/* form */
.form-panel{left:130px;top:384px;width:649px;height:450px;background:var(--grey-panel)}
.form-shadow{left:150px;top:830px;width:610px;height:16px;border-radius:50%;box-shadow:0 8px 10px rgba(0,0,0,.18)}
.label{position:absolute;right:487px;font-size:14px;color:#444}
.field{position:absolute;left:197px;width:387px;height:31px;background:var(--grey-field);border:1px solid #f6f6f6;box-shadow:0 1px 2px rgba(0,0,0,.12)}
.submit{position:absolute;left:197px;top:364px;width:387px;height:36px;background:var(--maroon);color:#fff;font-size:14px;text-align:center;line-height:36px;box-shadow:0 1px 2px rgba(0,0,0,.3)}
.brand-mark{left:832px;top:444px;width:238px;height:258px;border-radius:50%;background:radial-gradient(#d6d6d6,#c4c4c4 60%,#eee 72%)}

/* footer */
.footer-links{left:0;top:921px;width:1200px;height:41px;background:var(--grey-band);font-size:10.5px;color:#555;padding:13px 0 0 130px}
.footer-links em{font-style:normal;color:#d0007a}
.footer{left:0;top:962px;width:1200px;height:133px;background:linear-gradient(110deg,#e0148e 0%,#c4196e 35%,#8a1a55 42%,#c51f7e 50%,#b02a80 100%)}
.footer-nav a{position:absolute;top:28px;font-size:11px;color:#fff;text-decoration:none;letter-spacing:.5px}
.copyright{left:131px;top:79px;font-size:11px;color:#fff;letter-spacing:.5px}
.subscribe{left:828px;top:0;width:244px;height:133px;background:var(--magenta);color:#fff}
.subscribe h3{position:absolute;left:98px;top:26px;font-family:"Open Sans",sans-serif;font-weight:600;font-size:14.5px;line-height:18px;letter-spacing:.5px}
.sub-field{position:absolute;left:25px;top:73px;width:198px;height:26px;border:1px solid #fff;font-size:11.5px;padding:5px 6px}
.sub-go{position:absolute;right:0;top:0;width:35px;height:24px;background:#f2f2f2;color:#333;text-align:center;line-height:24px}
.sub-note{position:absolute;left:28px;top:106px;font-size:11.5px}
</style>
</head>
<body>

<header>
  <div class="abs brand"><span class="brand-dot"></span>VELI partners</div>
  <nav class="abs top-nav">
    <a style="left:30px">HOME</a>
    <a style="left:147px">ABOUT US</a>
    <a style="left:291px">WHAT WE DO</a>
    <a style="left:451px">BLOG</a>
    <a style="left:566px">CONTACT</a>
  </nav>
  <div class="abs dropdown">Industries<br>Expertise</div>
  <div class="abs search">Looking for something ?
    <span class="search-btn"><svg width="36" height="20" viewBox="0 0 36 20"><circle cx="16" cy="9" r="4.5" fill="none" stroke="#fff" stroke-width="1.6"/><line x1="19.5" y1="12" x2="23" y2="15" stroke="#fff" stroke-width="2"/></svg></span>
  </div>
</header>

<nav class="abs services">
  <div class="service" style="left:133px"><b>Corporate</b><span>Communications</span></div>
  <div class="sep" style="left:259px"></div>
  <div class="service" style="left:288px"><b>Digitilization</b><span>Technology Integration</span></div>
  <div class="sep" style="left:451px"></div>
  <div class="service" style="left:479px"><b>CSR</b><span>&nbsp;&amp; Sponsorships</span></div>
  <div class="sep" style="left:609px"></div>
  <div class="service" style="left:640px"><b>Investor Relations</b><span>And Fİnancial PR</span></div>
  <div class="sep" style="left:800px"></div>
  <div class="service" style="left:831px"><b>Strategic</b><span>Transactions</span></div>
  <div class="sep" style="left:938px"></div>
  <div class="service" style="left:972px"><b>Corporate</b><span>Governance</span></div>
</nav>

<section class="abs title-band">
  <div class="abs title-decor" role="img" aria-label="Faint brand pattern with circles"></div>
  <h1 class="abs page-title">Contact</h1>
  <svg class="abs" style="left:269px;top:28px" width="37" height="35" viewBox="0 0 37 35">
    <path d="M2 14 L18.5 2 L35 14 V33 H2 Z" fill="none" stroke="#fff" stroke-width="1.5"/>
    <rect x="8" y="6" width="21" height="16" fill="var(--maroon)" stroke="#fff" stroke-width="1.3"/>
    <line x1="12" y1="11" x2="25" y2="11" stroke="#fff"/><line x1="12" y1="15" x2="25" y2="15" stroke="#fff"/>
    <path d="M2 14 L18.5 25 L35 14" fill="none" stroke="#fff" stroke-width="1.5"/>
  </svg>
</section>

<main>
  <p class="abs intro">We are always looking to improve, and welcome any thoughts and feedback you may have.<br>Questions, comments, concerns, queries? <a href="#">Contact us</a> below!</p>

  <div class="abs form-shadow"></div>
  <form class="abs form-panel">
    <span class="label" style="top:51px">Name</span><span class="field" style="top:41px"></span>
    <span class="label" style="top:102px">Organization Name</span><span class="field" style="top:92px"></span>
    <span class="label" style="top:153px">Email</span><span class="field" style="top:143px"></span>
    <span class="label" style="top:204px">Phone</span><span class="field" style="top:194px"></span>
    <span class="label" style="top:247px">Message</span><span class="field" style="top:247px;height:82px"></span>
    <span class="submit">Submit</span>
  </form>

  <div class="abs brand-mark" role="img" aria-label="Large grey VELI partners brand symbol"></div>
</main>

<footer>
  <div class="abs footer-links"><em>Corporate Communications</em> / Digitilization and Technology Integration / CSR &amp; Sponsorships / Investor Relations and Fİnancial PR / Strategic Transactions / Corporate Governance</div>
  <div class="abs footer">
    <nav class="footer-nav">
      <a style="left:131px">HOME</a>
      <a style="left:196px">ABOUT US</a>
      <a style="left:289px">WHAT WE DO</a>
      <a style="left:397px">BLOG</a>
      <a style="left:461px">CONTACT</a>
    </nav>
    <div class="abs copyright">Copyright 2014 | Disclaimer | Privacy Policy</div>
    <div class="abs subscribe">
      <svg style="position:absolute;left:25px;top:26px" width="37" height="35" viewBox="0 0 37 35">
        <path d="M2 14 L18.5 2 L35 14 V33 H2 Z" fill="none" stroke="#fff" stroke-width="1.5"/>
        <rect x="8" y="6" width="21" height="16" fill="var(--magenta)" stroke="#fff" stroke-width="1.3"/>
        <line x1="12" y1="11" x2="25" y2="11" stroke="#fff"/><line x1="12" y1="15" x2="25" y2="15" stroke="#fff"/>
        <path d="M2 14 L18.5 25 L35 14" fill="none" stroke="#fff" stroke-width="1.5"/>
      </svg>
      <h3>Subscribe<br>for News Letters</h3>
      <div class="sub-field">Enter Your Email Address<span class="sub-go">GO</span></div>
      <div class="sub-note">Sign up now for more information</div>
    </div>
  </div>
</footer>

</body>
</html>
```